I need to redesign this website. Modern Fun Professional Redesign For www.JollyPerkHub.com = New Name www.ClaimVouchly.com

Use existing content as it is on website exactly and we will revise after initial mock ups.

The new name will be ClaimVouchly.com please make a quick logo for this site too while redesigning.

Make it look like an official website....

Target Market(s)

Consumers that are redeeming certificates that businesses gave to them as a gift for customer loyalty,e tc.

Industry/Entity Type

It Professional

Logo Text

www.ClaimVouchly.com

Number of Pages Required

4 page

Colors

Designer to choose colors to be used in the design.

Requirements
Must have
• Must look professional, build trust and credibility.
Nice to have
• open
Should not have
• open

```html
<!DOCTYPE html>
<html lang="en">
<head>
<meta charset="utf-8">
<title>ClaimVouchly.com – Home</title>
<link rel="stylesheet" href="https://fonts.googleapis.com/css2?family=Open+Sans:wght@300;400;600;700&family=Ubuntu:wght@400;500;700&family=Pacifico&display=swap">
<style>
:root{
  --teal:#1b6f87;
  --cyan:#29b5e8;
  --cyan-soft:#e9f8fc;
  --band:#b9e6f8;
  --green:#6aa431;
  --green-dark:#2f7d1d;
  --orange:#e0701b;
  --orange-dark:#c8560d;
  --grey:#8a8a8a;
  --text:#555;
  --ink:#1f3a4a;
  --white:#fff;
}
*{box-sizing:border-box;margin:0;padding:0}
html,body{width:1200px;height:1200px;overflow:hidden;background:#fff;font-family:"Open Sans",sans-serif;color:var(--text)}
.page{position:absolute;left:288px;top:0;width:620px;height:1200px;background:#fff;box-shadow:0 0 18px rgba(0,0,0,.45);overflow:hidden}
.abs{position:absolute}

/* header */
.site-header{left:0;top:0;width:620px;height:44px;background:#fff}
.brand{left:92px;top:10px;display:flex;align-items:center;gap:5px;font-family:"Ubuntu",sans-serif;font-weight:700;font-size:16px;color:var(--green-dark)}
.brand-dot{width:10px;height:10px;border-radius:50%;background:var(--green)}
.nav{left:298px;top:18px;display:flex;gap:8px;font-size:6.6px;color:var(--grey);letter-spacing:.2px}
.nav .active{color:var(--green-dark)}

/* hero */
.hero{left:0;top:44px;width:620px;height:254px;background:linear-gradient(180deg,#6d8a5a 0%,#4f6b3a 30%,#3d5a3a 58%,#3f6f87 78%,#2f5668 100%)}
.hero-live{left:95px;top:56px;font-family:"Pacifico",cursive;font-size:68px;color:#fff;line-height:1}
.hero-title{left:98px;top:116px;font-family:"Ubuntu",sans-serif;font-weight:500;font-size:19px;line-height:20px;color:#fff;letter-spacing:.5px}
.hero-sub{left:98px;top:192px;width:180px;font-size:10px;line-height:14px;color:rgba(255,255,255,.25);font-weight:600}
.arrow{width:16px;height:16px;border-radius:50%;background:rgba(255,255,255,.35)}

/* call bar */
.callbar{left:0;top:298px;width:620px;height:46px;background:var(--teal);color:#fff}
.call-label{left:44px;top:14px;font-family:"Ubuntu",sans-serif;font-weight:700;font-size:13.5px}
.call-note{left:66px;top:32px;font-size:5.6px}
.call-phone{left:188px;top:8px;font-family:"Ubuntu",sans-serif;font-weight:700;font-size:25px;letter-spacing:.5px}
.cert-title{left:392px;top:3px;font-size:4.8px;font-weight:700;color:#0d2b37}
.cert-note{left:400px;top:9px;font-size:3.8px;color:#bfe3ee}
.cert-form{left:378px;top:15px;width:194px;height:26px;background:var(--green-dark);padding:3px}
.cert-input{left:5px;top:4px;width:146px;height:18px;background:#fff}
.cert-go{left:154px;top:4px;width:36px;height:18px;background:#8fc22e;color:#234;font-size:10px;text-align:center;line-height:18px}

/* about */
.about{left:0;top:344px;width:620px;height:188px;background:linear-gradient(120deg,#b9b4ad 0%,#d9d2c2 35%,#e4dcc8 60%,#cfd7cf 100%)}
.about-tab{left:265px;top:0;width:88px;height:42px;background:#8db63e;color:#fff;font-family:"Ubuntu",sans-serif;font-weight:700;font-size:12px;text-align:center;line-height:54px;letter-spacing:.5px}
.about-goal{left:282px;top:48px;font-size:5.5px;letter-spacing:2px;color:#9a9a9a}
.about-box{left:121px;top:84px;width:378px;height:54px;background:rgba(41,181,232,.88);color:#0f2632;font-size:6.4px;line-height:9px;text-align:center;padding-top:7px}
.about-rule{left:288px;top:140px;width:42px;height:2px;background:#333}
.travel-id{left:272px;top:158px;font-size:5.6px;font-weight:700;color:#222}

/* offers */
.sec-title{left:0;width:620px;text-align:center;font-family:"Ubuntu",sans-serif}
.offers-title{top:562px;font-size:18px;font-weight:500;color:var(--grey);letter-spacing:.8px}
.offers-sub{top:592px;font-size:11.5px;font-weight:300;color:var(--grey);font-family:"Open Sans",sans-serif}
.offer{width:130px;top:617px}
.offer-date{left:0;top:0;width:32px;height:32px;border-radius:50%;color:#fff;font-size:7.5px;text-align:center;line-height:32px}
.offer-name{left:38px;top:5px;font-family:"Ubuntu",sans-serif;font-weight:500;font-size:10px;color:#28414c;white-space:nowrap}
.offer-nights{left:38px;top:17px;font-size:7px;color:var(--grey);white-space:nowrap}
.offer-text{left:4px;top:40px;width:124px;font-size:4.7px;line-height:8.8px;color:#777}
.offer-more{left:4px;top:91px;font-size:4.8px;color:var(--green-dark)}

/* plans */
.plans-title{top:744px;font-size:17.5px;font-weight:500;color:var(--grey);letter-spacing:.5px}
.plan-label{top:784px;width:155px;text-align:center;font-size:8px;color:var(--grey);letter-spacing:.3px}
.plan-img{top:798px;width:155px;height:143px}
.plan-cta{left:310px;top:798px;width:155px;height:143px;background:#2a9fd0;color:#fff;text-align:center}
.cta-head{left:0;top:26px;width:155px;font-weight:700;font-size:7.5px}
.cta-text{left:18px;top:43px;width:120px;font-size:6.2px;line-height:9px}
.cta-rule{left:66px;top:84px;width:22px;height:1px;background:#fff}
.cta-btn{left:51px;top:90px;width:52px;height:16px;border:1px solid #fff;font-size:4.6px;font-weight:700;line-height:14px}
.cta-icons{left:44px;top:117px;display:flex;gap:12px}
.cta-icons span{width:14px;height:14px;border:1px solid #fff;border-radius:50%}

/* testimonials */
.testi{left:0;top:941px;width:620px;height:259px;background:var(--cyan-soft)}
.testi-band{left:464px;top:0;width:130px;height:259px;background:var(--band)}
.testi-head{left:50px;top:22px;font-family:"Ubuntu",sans-serif;font-weight:500;font-size:11px;color:var(--orange-dark);letter-spacing:.3px}
.testi-kicker{left:50px;top:39px;font-size:6px;color:var(--green)}
.card{top:51px;width:120px;height:180px;background:#fff;border:1px solid #e2e2e2}
.card-img{left:0;top:0;width:118px;height:70px}
.card-place{left:6px;top:74px;font-family:"Ubuntu",sans-serif;font-size:8px;font-weight:500;color:#2a3a44}
.card-added{left:6px;top:85px;font-size:3px;color:#777}
.card-text{left:6px;top:93px;width:108px;font-size:4.6px;line-height:8.5px;color:#777}
.card-more{left:6px;top:155px;font-size:4.6px;color:var(--green-dark)}
.card-meta{left:0;top:168px;width:118px;height:11px;border-top:1px solid #eee;font-size:2.8px;color:#aaa;padding:4px 6px;display:flex;gap:10px}
.quote{left:449px;width:145px}
.quote-img{left:0;top:0;width:29px;height:27px}
.quote-text{left:21px;top:-2px;width:100px;font-size:3.5px;line-height:4.5px;color:#223}
.quote-rule{height:1px;background:#556;left:40px;width:62px}
.see-more{left:483px;top:237px;width:97px;height:18px;background:var(--orange);color:#fff;font-size:6.2px;font-weight:700;text-align:center;line-height:18px;letter-spacing:.3px}
</style>
</head>
<body>
<div class="page">

  <header class="abs site-header">
    <div class="abs brand"><span class="brand-dot"></span>ClaimVouchly</div>
    <nav class="abs nav">
      <span class="active">HOME</span><span>PLANS</span><span>TESTIMONIALS</span><span>ABOUT US</span><span>VIDEOS</span><span>TERMS</span><span>CONTACTS</span>
    </nav>
  </header>

  <section class="abs hero" role="img" aria-label="Cruise ship sailing through a green fjord beside a waterfall and snowy mountains">
    <div class="abs hero-live">Live</div>
    <div class="abs hero-title">THE VACATION<br>OF YOUR DREAMS</div>
    <div class="abs hero-sub">Redeem your certificate and enjoy the dream vacation of yours</div>
    <div class="abs arrow" style="left:21px;top:118px"></div>
    <div class="abs arrow" style="left:591px;top:118px"></div>
  </section>

  <section class="abs callbar">
    <div class="abs call-label">CALL US NOW AT</div>
    <div class="abs call-note">Get more info when you want</div>
    <div class="abs call-phone">555-014-2290</div>
    <div class="abs cert-title">PLEASE ENTER A VALID CERTIFICATE ID IN THE FORM BELOW</div>
    <div class="abs cert-note">To redeem your certificate and to view FAQs, terms and locations</div>
    <div class="abs cert-form">
      <div class="abs cert-input"></div>
      <div class="abs cert-go">Go</div>
    </div>
  </section>

  <section class="abs about" role="img" aria-label="Travel desk with a map, camera, compass, notebook and hands planning a trip">
    <div class="abs about-tab">ABOUT US</div>
    <div class="abs about-goal">whats our goals</div>
    <div class="abs about-box"><b>ClaimVouchly</b>, is a leading travel certificate fulfillment company<br>dedicated to providing the best Scheduled Vacations service.<br>We are extremely proud to do what is right in order to offer<br>the best service to our customers.</div>
    <div class="abs about-rule"></div>
    <div class="abs travel-id">TRAVEL ID # CST 4417380</div>
  </section>

  <h2 class="abs sec-title offers-title">LIVE THE DREAM VACATION, BOOK IT NOW</h2>
  <p class="abs sec-title offers-sub">Some offers that may interest you</p>

  <article class="abs offer" style="left:98px">
    <div class="abs offer-date" style="background:#3dbb3f">05|07</div>
    <div class="abs offer-name">Las Vegas</div>
    <div class="abs offer-nights">2 wonderfull night</div>
    <p class="abs offer-text">Travel to Las Vegas, or any other city in the United States. Included in this certificate are 2 round trip air tickets for 2 adults with 2 nights accommodation in selected hotels and selected cities. Plus a choice of 3, 4 or 7 night cruise for 2 persons.</p>
    <div class="abs offer-more">More Information</div>
  </article>
  <article class="abs offer" style="left:249px">
    <div class="abs offer-date" style="background:#2bb6e6">03|09</div>
    <div class="abs offer-name">Brandson Misouri</div>
    <div class="abs offer-nights">2 wonderfull night</div>
    <p class="abs offer-text">Spend 2 nights in Branson, Missouri. With clean room and comfortable beds. Wonderful tour of the property and enjoy beautiful scenery, beautiful, well maintained and clean gardens. You will definitely want to go back there again."</p>
    <div class="abs offer-more">More Information</div>
  </article>
  <article class="abs offer" style="left:400px">
    <div class="abs offer-date" style="background:#f26a1d">01|11</div>
    <div class="abs offer-name">New Orleans</div>
    <div class="abs offer-nights">2 wonderfull night</div>
    <p class="abs offer-text">Enjoy our certificate, 3 nights and two days in a wonderful hotel conveniently located, opposite the super dome, French quarters and excellent public transport. Have fun and relax in the best rooms. Holidays worth it at an excellent cost."</p>
    <div class="abs offer-more">More Information</div>
  </article>

  <h2 class="abs sec-title plans-title">Choose your best holiday plans</h2>
  <div class="abs plan-label" style="left:0">FRIENDSHIP PLANS</div>
  <div class="abs plan-label" style="left:155px">FAMILY PLANS</div>
  <div class="abs plan-label" style="left:310px">BUSINESS VACATION</div>
  <div class="abs plan-label" style="left:465px">LOVE VACATIONS PLANS</div>
  <div class="abs plan-img" style="left:0;background:linear-gradient(135deg,#d9c7a6,#b79a7a 50%,#8fa9b8)" role="img" aria-label="Group of smiling friends taking a selfie in a sunny city"></div>
  <div class="abs plan-img" style="left:155px;background:linear-gradient(180deg,#8cc4e4,#5fa2c8 45%,#c9a88a)" role="img" aria-label="Family playing together in the sea on a beach"></div>
  <div class="abs plan-cta">
    <div class="abs cta-head">We help you in process</div>
    <div class="abs cta-text">Choose the way in which you will travel and with whom you will do, make your exciting holiday dreams come true with ClaimVouchly</div>
    <div class="abs cta-rule"></div>
    <div class="abs cta-btn">FILL OUR FORM</div>
    <div class="abs cta-icons"><span></span><span></span><span></span></div>
  </div>
  <div class="abs plan-img" style="left:465px;width:156px;background:linear-gradient(135deg,#cdb99a,#b38d6d 50%,#8d7a6a)" role="img" aria-label="Couple on holiday taking a photo together in an old town"></div>

  <section class="abs testi">
    <div class="abs testi-band"></div>
    <h2 class="abs testi-head">WHAT OUR CLIENTS ARE SAYING ABOUT US</h2>
    <div class="abs testi-kicker">TESTIMONIALS</div>

    <article class="abs card" style="left:50px">
      <div class="abs card-img" style="background:linear-gradient(180deg,#7fa9b4,#b9b2a4)" role="img" aria-label="Traveller sitting on seaside rocks"></div>
      <div class="abs card-place">Port Orange, FL</div>
      <div class="abs card-added">FL / Added on 10/12/2015 11:22:28 am</div>
      <p class="abs card-text">"My vacation was excellent! We started in Milano, and visited the Duomo Cathedral; then we went to Lako Como, and then proceeded to Sorrento; Amalfi; Positano; Bari and ended in the Abbruzzi area. Wonderful people, weather, great food and great wine!"</p>
      <div class="abs card-more">More Reading →</div>
      <div class="abs card-meta"><span>Anne C.</span><span>12 July 2015</span><span>See more content</span></div>
    </article>
    <article class="abs card" style="left:178px">
      <div class="abs card-img" style="background:linear-gradient(180deg,#b9c2c4,#8e9a9a 60%,#a8a48f)" role="img" aria-label="City hotels viewed from a hotel room window"></div>
      <div class="abs card-place">Austin Texas</div>
      <div class="abs card-added">Added on 09/24/2015 02:30:19 pm</div>
      <p class="abs card-text">"My vacation was excellent. The photo I have enclosed is the view I saw from my lovely room when I enjoyed Las Vegas with a friend last November! The weather was perfect. The entertainment options were outstanding!"</p>
      <div class="abs card-more">More Reading →</div>
      <div class="abs card-meta"><span>Tom R.</span><span>12 July 2015</span><span>See more content</span></div>
    </article>
    <article class="abs card" style="left:307px">
      <div class="abs card-img" style="background:linear-gradient(180deg,#1f2e4a,#3b4a6a 60%,#6b5a55)" role="img" aria-label="Couple posing in front of city lights at night"></div>
      <div class="abs card-place">Van Nuys, CA</div>
      <div class="abs card-added">Added on 09/24/2015 02:32:30 pm</div>
      <p class="abs card-text">"I am extremely happy with my service, everything worked out perfect. My wife and I had a great time in Las Vegas. The hotel we stayed at was very nice and clean. I would go there again. Thank you for everything."</p>
      <div class="abs card-more">More Reading →</div>
      <div class="abs card-meta"><span>Jose G.</span><span>12 July 2015</span><span>See more content</span></div>
    </article>

    <div class="abs quote" style="top:47px">
      <div class="abs quote-img" style="background:#b8a894" role="img" aria-label="Guest photo at a hotel"></div>
      <p class="abs quote-text" style="left:37px">"Our vacation was great… We had a tremendous time in New Orleans. Our hotel stay was wonderful. It was conveniently located across from the super dome, French quarters and public transportation. My wife and I haven't had this much fun in a long time. This vacation was well worth the money!"<br><b>Dale M.</b><br>SE Grand Rapids, MI<br>Added on 08/15/2014 04:13:25 pm</p>
      <div class="abs quote-rule" style="top:47px"></div>
    </div>
    <div class="abs quote" style="top:102px">
      <div class="abs quote-img" style="background:#c9a58a" role="img" aria-label="Honeymoon couple photo"></div>
      <p class="abs quote-text" style="left:37px">"We went to the Palm Cove resort in Costa Rica last year for our honeymoon. It was AMAZING!! Full of dirt bikes, zip lining, horseback riding, monkeys, volcano hot pools, and the most amazing resort tucked in the jungles of Costa Rica. Wouldn't change a minute of it!"<br><b>Monica L</b><br>Charlotte, NC<br>Added on 07/21/2014 12:44:08 pm</p>
      <div class="abs quote-rule" style="top:52px"></div>
    </div>
    <div class="abs quote" style="top:167px">
      <div class="abs quote-img" style="background:#a98b7a" role="img" aria-label="Couple on a Las Vegas trip"></div>
      <p class="abs quote-text" style="left:37px">"This past June, my husband Derek and I were able to go to Las Vegas. A place we always wanted to see but weren't sure we could afford! We stayed on the strip, toured Old Vegas and visited the Hoover Dam. Thanks for a fun and relaxing get-away!"<br><b>Paula R</b><br>Durham, NC<br>Added on 07/21/2014 11:58:15 am</p>
    </div>

    <div class="abs see-more">SEE MORE TESTIMONIALS</div>
  </section>

</div>
</body>
</html>
```